New York Property Management Company needs a Brochure Designed

We need a brochure for a new property management company in New York called KT7 Realty Partners. The 2 is superscript (squared.) We are looking for buildings to manage and want to showcase our expertise and caring. Logo is attached. We are getting a different photo and do not need all the verbiage. Also, does not need to be a trifold.
Updates

Property management group is a RESIDENTIAL property management group. I neglected to mention that. Thanks.

Hi designers, We've received very few designs so far so we've extended the deadline. We're hoping to receive your creative submissions soon! Thank you!

Reason: A few people have to weigh in on the design and it has been difficult coordinating this. We are getting close to making a decision and just need a few more days.

Industry/Entity Type

Property Management

```html
<!DOCTYPE html>
<html lang="en">
<head>
<meta charset="utf-8">
<title>KT7 Realty Partners – Brochure</title>
<link href="https://fonts.googleapis.com/css2?family=Didact+Gothic&family=Mulish:wght@700&display=swap" rel="stylesheet">
<style>
  :root{
    --stage:#000000;
    --paper:#ebebeb;
    --slate:#4b5155;
    --slate-soft:#5b6166;
    --ink:#4a4a4a;
    --orange:#f2901e;
    --amber:#fbb917;
    --yellow:#fcd20f;
    --white:#ffffff;
    --label:#bdbdbd;
  }
  *{box-sizing:border-box;margin:0;padding:0}
  html,body{width:1200px;height:900px;overflow:hidden;background:var(--stage)}
  body{position:relative;font-family:"Didact Gothic",sans-serif;color:var(--ink)}
  .page{position:absolute;background:var(--paper);overflow:hidden}
  .page--front{left:37px;top:43px;width:560px;height:770px}
  .page--back{left:611px;top:40px;width:560px;height:775px}
  .page-label{position:absolute;top:848px;width:200px;text-align:center;font-size:24px;color:var(--label)}
  .page-label--front{left:226px}
  .page-label--back{left:782px}

  .brand{position:absolute;left:35px;top:22px;width:115px;height:115px;border:4px solid var(--white);outline:1px solid #cfcfcf;background:var(--slate);display:flex;align-items:center;justify-content:center;text-align:center;padding:8px}
  .brand-name{font-size:17px;line-height:1.2;color:var(--white)}

  .body-copy{font-size:9.3px;line-height:11.6px}
  .body-copy p{margin-bottom:11.6px}
  .intro{position:absolute;left:37px;top:152px;width:240px}

  .values{position:absolute;left:312px;top:0;width:229px;height:480px;background:linear-gradient(180deg,var(--orange) 20%,var(--amber) 100%)}
  .values-cap{height:72px;background:var(--slate)}
  .values-copy{color:var(--white);padding:14px 5px 0 5px;font-size:9.1px;line-height:11.6px}
  .values-copy .lead{text-align:justify;margin-bottom:10px}
  .values-copy ul{list-style:none}
  .values-copy li{position:relative;padding-left:13px;margin-bottom:10px}
  .values-copy li::before{content:"•";position:absolute;left:2px}

  .stripes{position:absolute;left:0;top:0}
  .city-band{position:absolute;left:0;width:560px;background:linear-gradient(180deg,var(--slate-soft) 0%,var(--slate) 40%)}
  .city-band--front{top:606px;height:164px}
  .city-band--back{top:700px;height:75px}

  .front-footer{position:absolute;left:0;width:560px;text-align:center;color:var(--white);font-size:13px;line-height:16px}
  .front-footer--address{top:690px}
  .front-footer--web{top:739px}

  .glow{position:absolute;left:0;top:0}
  .bio{position:absolute;top:42px;font-size:9.3px;line-height:11.6px}
  .bio h2{font-family:"Mulish",sans-serif;font-size:11px;font-weight:700;margin-bottom:14px;color:var(--ink)}
  .bio p{margin-bottom:11.6px}
  .bio--left{left:20px;width:250px}
  .bio--right{left:299px;width:245px}
  .team-photo{position:absolute;left:44px;top:453px;width:211px;height:247px;background:linear-gradient(160deg,#c9ccd0 0%,#8e969c 45%,#4f5459 100%)}
</style>
</head>
<body>

<section class="page page--front">
  <div class="values">
    <div class="values-cap"></div>
    <div class="values-copy">
      <p class="lead">Every cooperative, condominium and rental building has a structure and physical plant that needs ongoing attention from ownership, management, staff and outside professionals. In order for building operations and projects to flow smoothly, these components must work collaboratively. Management is the centerpiece of this equation. KT7RP provides bespoke management solutions to all buildings in its portfolio.</p>
      <ul>
        <li>Shareholders, unit owners and tenants are all individuals who have a home that needs the appropriate level of management to ensure a quiet, safe and well-maintained environment.</li>
        <li>We manage multifamily dwellings the way they should be managed watching costs, providing quality service, creating value. We create value for building resulting in increased apartment/building values.</li>
        <li>We leverage knowledge of real estate ownership, management and development to maximize appreciation and income</li>
        <li>We believe that quality management equals integrity, accountability, ownership, reliability and responsibility.</li>
        <li>We attract top-notch managers by providing ownership opportunities and income generating potential.</li>
      </ul>
    </div>
  </div>

  <svg class="stripes" width="560" height="770" viewBox="0 0 560 770" aria-hidden="true">
    <g fill="var(--yellow)">
      <rect x="312" y="492" width="230" height="25"/>
      <rect x="312" y="527" width="230" height="20"/>
      <rect x="312" y="558" width="230" height="18"/>
      <rect x="312" y="587" width="230" height="15"/>
    </g>
  </svg>

  <div class="city-band city-band--front" role="img" aria-label="City skyline silhouette in dark slate along the bottom of the page"></div>

  <div class="brand"><span class="brand-name">KT7 Realty Partners</span></div>

  <div class="intro body-copy">
    <p>At KT7 Realty Partners, we manage each building as if it were our own; return each phone call; respond to each email; negotiate the best possible pricing on goods and services; address building needs in a respectful, practical, efficient and economic manner.</p>
    <p>We manage buildings with the highest level of service. Management is about service; it is knowing the operations of a building, but it is so much more. It is understanding resident and owner needs, identifying opportunities for creating value and providing a well-run and supportive community.</p>
    <p>Management encompasses all building services including, but not limited to, billing, collections, staff management, maintenance, compliance, capital projects and communication with owners, residents, vendors and building professionals. We do this by using established, reputable and reliable business partners.</p>
    <p>In order for our philosophy to succeed, a manager must be more than just an employee. KT7RP provides growth opportunities that motivate staff for long-term potential and retention. The team is important for sharing of expertise, knowledge and experience. We are engaged as a team on each and every property.</p>
  </div>

  <p class="front-footer front-footer--address">KT7 Realty Partners, LLC&nbsp; 14 East 52nd St., Ste. 410&nbsp; New York, NY&nbsp; 10022<br>212.555.0147</p>
  <p class="front-footer front-footer--web">www.KT7RP.com</p>
</section>

<section class="page page--back">
  <svg class="glow" width="560" height="775" viewBox="0 0 560 775" aria-hidden="true">
    <defs>
      <linearGradient id="back-glow" x1="0" y1="0" x2="1" y2="0.3">
        <stop offset="0" stop-color="var(--orange)"/>
        <stop offset="0.65" stop-color="var(--yellow)"/>
        <stop offset="1" stop-color="var(--amber)"/>
      </linearGradient>
    </defs>
    <rect width="560" height="775" fill="url(#back-glow)"/>
    <path fill="var(--paper)" d="M0,0 L560,0 L560,562 L289,550 L289,436 L269,436 L0,415 Z"/>
  </svg>

  <div class="team-photo" role="img" aria-label="Photo of the two founders standing on a city rooftop terrace"></div>

  <div class="city-band city-band--back" role="img" aria-label="City skyline silhouette in dark slate along the bottom of the page"></div>

  <article class="bio bio--left">
    <h2>Marcus Hale</h2>
    <p>Prior to co-founding KT7 Realty Partners, Marcus was the Acquisitions Manager and a Senior Property Manager at Harborline Residential New York, LLC (formerly Astor Row Realty, Inc.) managing properties and locating investment opportunities for the principals of Harborline. Marcus used his management, investment and development knowledge to create and implement asset repositioning plans including renovations and re-leasing for investments in order to maximize value for investors. Marcus has managed over 1200 units in more than 30 buildings including residential and commercial owners/tenants and 50+ staff members.</p>
    <p>Marcus has experience in high end and affordable housing including rent stabilized units in the rental, coop and condo markets both from Harborline and his prior position at The Calloway Group in Washington, DC. He began working in property management upon graduation from Chesapeake State University with a degree in Economics. Marcus grew up in Minneapolis, MN.</p>
    <p>Marcus established himself as a leading manager and key investment advisor at Harborline. He is an entrepreneur and is parlaying his unique skills and knowledge into making KT7 one of New York City's leading property management and real estate investment firms.</p>
  </article>

  <article class="bio bio--right">
    <h2>Renata Solis</h2>
    <p>Before co-founding KT7 Realty Partners, Renata was a Team Leader at Harborline Residential (formerly Astor Row), managing a team of 10+ managers responsible for a portfolio of multi-family building varying in size, location and prominence in Manhattan, Riverdale and Queens. She has been in property management for 12 years. She also served as Vice President of Client Accounting, utilizing her accounting background and management experience to restructure the department to better serve Astor Row clients.</p>
    <p>Renata has over 20 years of experience in various aspects of the management business. She was Board President of a large Westside Manhattan cooperative for more than 10 years. She began her career in New York at Meridian Card Services in finance, accounting and marketing positions. Her passion and interest in the management business prompted her to change careers and she joined a small management company in 2002. She rose through the ranks to both lead Client Accounting and her management team.</p>
    <p>Renata is originally from San Diego, California, where she obtained her Certified Public Accounting license while working for Whitcombe &amp; Lane. She moved to New York where she earned her Masters in Business Administration (finance) from Hudson Heights University. Her undergraduate degree is in accounting from Pacific Coast University.</p>
    <p>During Renata's tenure at Harborline/Astor Row, she established herself as a high performing manager and leader. Her broad scope of experience and education continue to be utilized by many buildings in improving financial performance, building operations and staff management. She is continuing to leverage these skills in building KT7RP.</p>
  </article>
</section>

<p class="page-label page-label--front">front</p>
<p class="page-label page-label--back">back</p>

</body>
</html>
```